Bday party

UPDATED: Club flyer for Velvet's four year anniversary (main) and my birthday party (secondary). I have photos and logos. I will include a copy of a flyer I recently had done through artfolkhub.com that was perfect and i purchased it (ember mondays). I really like modern designs with a non-slutty girl. The girl is not mandatory though if it looks better without. Here is the text (also I attached a flyer for the main room of the club):

Velvet Nightclub's Four Year Anniversary

Also celebrating
KORVAN' BDAY

Pure House Music on the patio featuring
KORVAN
DELMA

Saturday 11/17 10p-2a

Congrats to the Newlyweds Trevor and Lorna (Pelham)!
Updates

I changed the focus from my bday to Velvet's four year anniversary so that is the main focus.  The non-slutty girl is not mandatory, it can be just graphics if that looks better.  I really like the sample flyer I attached as well.  Thanks.  

Industry/Entity Type

Club

Requirements
Should not have
• Anything too sexual (a cute girl on the flyer is fine but nothing too sexy)

```html
<!DOCTYPE html>
<html lang="en">
<head>
<meta charset="utf-8">
<title>Velvet Nightclub – 4 Year Anniversary</title>
<link rel="stylesheet" href="https://fonts.googleapis.com/css2?family=Alfa+Slab+One&family=Sansita:wght@800;900&family=Lobster&family=Cinzel:wght@400&display=swap">
<style>
  :root {
    --ink: #000000;
    --cream: #f4f0c4;
    --gold-hi: #fbf6c8;
    --gold-lo: #8f8745;
    --red-hi: #ff6a5a;
    --red-lo: #c8121c;
    --white: #ffffff;
    --grey: #5a5a5a;
  }
  * { margin: 0; padding: 0; box-sizing: border-box; }
  html, body { width: 927px; height: 1200px; overflow: hidden; background: var(--ink); }
  .flyer {
    position: relative; width: 927px; height: 1200px; overflow: hidden;
    background: radial-gradient(ellipse at 50% 95%, #1e1e1e 0%, var(--ink) 60%);
    font-family: "Sansita", sans-serif;
  }
  .hero-photo {
    position: absolute; left: 0; top: 0; width: 927px; height: 720px;
    background:
      radial-gradient(ellipse 22% 28% at 64% 30%, #e8e8e8 0%, #9a9a9a 45%, transparent 75%),
      radial-gradient(ellipse 18% 22% at 90% 38%, rgba(190,90,200,.55) 0%, rgba(60,160,220,.35) 50%, transparent 80%),
      radial-gradient(ellipse 30% 45% at 14% 35%, #3a3a3a 0%, transparent 70%),
      radial-gradient(ellipse 60% 60% at 60% 50%, #2a2a2a 0%, #0a0a0a 70%);
  }
  .text { position: absolute; width: 100%; white-space: nowrap; }
  .date-day { left: 0; top: 102px; width: 468px; text-align: center; font-size: 45px; font-weight: 900; color: var(--cream); }
  .date-time { left: 0; top: 180px; width: 468px; text-align: center; font-size: 50px; font-weight: 900; color: var(--cream); letter-spacing: 2px; }
  .patio { left: 50px; top: 258px; width: auto; font-size: 27px; font-weight: 800; color: var(--cream); line-height: 36px; }
  .dj-main {
    left: 112px; top: 350px; width: auto; font-family: "Alfa Slab One", serif; font-size: 52px;
    background: linear-gradient(var(--red-hi), var(--red-lo)); -webkit-background-clip: text; background-clip: text; color: transparent;
  }
  .dj-guest { left: 150px; top: 440px; width: auto; display: flex; align-items: center; gap: 10px; font-size: 30px; font-weight: 800; color: var(--white); }
  .dj-guest .dot { width: 18px; height: 18px; border-radius: 50%; border: 3px solid var(--white); }
  .headline-years {
    left: 0; top: 650px; text-align: center; font-family: "Alfa Slab One", serif; font-size: 128px; line-height: 1;
    background: linear-gradient(var(--gold-hi) 20%, var(--gold-lo)); -webkit-background-clip: text; background-clip: text; color: transparent;
    padding-left: 20px;
  }
  .headline-anniv { left: 0; top: 778px; text-align: center; padding-left: 120px; font-family: "Lobster", cursive; font-size: 62px; color: #d9d7a0; transform: skewX(-8deg); }
  .venue { left: 104px; top: 880px; width: auto; font-family: "Cinzel", serif; font-size: 50px; color: var(--white); line-height: 1; }
  .venue-sub { left: 136px; top: 934px; width: auto; font-family: "Cinzel", serif; font-size: 16px; letter-spacing: 8px; color: var(--white); }
  .also { left: 458px; top: 885px; width: auto; font-size: 40px; font-weight: 800; color: #e2e4a8; }
  .bday {
    left: 0; top: 955px; text-align: center; font-family: "Alfa Slab One", serif; font-size: 72px; letter-spacing: 3px; padding-left: 40px;
    background: linear-gradient(var(--red-hi) 10%, var(--red-lo)); -webkit-background-clip: text; background-clip: text; color: transparent;
  }
  .rules { position: absolute; left: 0; top: 1050px; }
  .congrats { left: 0; top: 1112px; text-align: center; font-size: 26px; font-weight: 800; color: var(--cream); }
</style>
</head>
<body>
<main class="flyer">
  <div class="hero-photo" role="img" aria-label="Black and white photo of a woman in profile wearing colourful glowing headphones, with a faint second profile on the left"></div>

  <p class="text date-day">Saturday</p>
  <p class="text date-time">11/17 10p-2a</p>
  <p class="text patio">Pure House Music On<br>the patio featuring</p>
  <p class="text dj-main">KORVAN</p>
  <p class="text dj-guest"><span class="dot"></span>DELMA</p>

  <p class="text headline-years">4 YEAR</p>
  <p class="text headline-anniv">Anniversary</p>

  <p class="text venue">VELVET</p>
  <p class="text venue-sub">NIGHTCLUB</p>
  <p class="text also">Also celebrating</p>
  <p class="text bday">KORVAN' BDAY</p>

  <svg class="rules" width="927" height="40" viewBox="0 0 927 40" aria-hidden="true">
    <line x1="0" y1="8" x2="927" y2="8" stroke="var(--grey)" stroke-width="3"/>
    <line x1="0" y1="30" x2="927" y2="30" stroke="var(--grey)" stroke-width="3"/>
  </svg>

  <p class="text congrats">Congrats to the Newlyweds Trevor and Lorna (Pelham)!</p>
</main>
</body>
</html>
```